Flyer-Design für innovativen Anbieter von E-Mobilität
Zielgruppe
Wir sind ein innovativer Anbieter von E-Mobilität und bieten Erlebnisse, Seminare und Fahrzeugmieten an. Unsere Zielgruppe sind Endverbraucher, die oftmals noch keine größere Erfahrung mit E-Mobilität haben, diese aber kennenlernen wollen. Darüber hinaus sind auch Touristen und Besucher unsere Zielgruppe.
Aufgabenstellung
Der Flyer sollte zwingend das Thema Ökologie/Nachhaltigkeit berücksichtigen. Zudem soll es emotional ansprechend sein. Bei den Texten liegt eine Vorlage anbei, wobei wir gerne auch einen neuen Ansatz verfolgen würden. Der Flyer sollte in Deutsch und Englisch gehalten sein.

```html
<!DOCTYPE html>
<html lang="de">
<head>
<meta charset="utf-8">
<title>Stromwerk – Erlebnisse &amp; Seminare</title>
<link href="https://fonts.googleapis.com/css2?family=Arimo:wght@400;700&display=swap" rel="stylesheet">
<style>
:root{
  --green:#5cb82e;
  --blue:#1c2f7f;
  --ink:#1d1d1d;
  --paper:#ffffff;
  --bg:#eeeeee;
  --rule:#e2e2e2;
}
*{box-sizing:border-box;margin:0;padding:0}
html,body{width:901px;height:1200px;overflow:hidden}
body{background:var(--bg);font-family:"Arimo",Arial,sans-serif;color:var(--ink);position:relative}
.flyer{position:absolute;left:15px;top:292px;width:870px;height:616px;background:var(--paper);display:flex;box-shadow:0 4px 14px rgba(0,0,0,.18)}
.panel{position:relative;width:290px;height:100%;border-right:1px solid var(--rule)}
.panel:last-child{border-right:none}
.brand{font-weight:700;color:var(--blue);white-space:nowrap}
.brand-small{position:absolute;right:14px;top:14px;font-size:11px}
.brand-large{position:absolute;left:34px;top:26px;font-size:30px;display:flex;align-items:center;gap:7px}
.brand-large .dot{width:14px;height:14px;border-radius:50%;background:var(--green)}
.tagline{position:absolute;left:36px;top:96px;font-size:8px;font-weight:700;color:var(--green)}
.headline{position:absolute;left:36px;top:108px;font-size:17px;font-weight:700;color:var(--blue)}
.hero{position:absolute;left:0;top:150px}
.slogan{position:absolute;left:0;right:0;top:530px;text-align:center;font-size:13px;color:var(--blue)}
.url-bar{position:absolute;top:563px;left:50%;transform:translateX(-50%);width:166px;height:17px;background:var(--green);color:#fff;font-size:11.5px;text-align:center;line-height:17px}
.offers{position:absolute;left:22px;top:58px;list-style:none}
.offer{display:flex;gap:12px;height:82px}
.offer-photo{width:96px;height:69px;flex:none}
.offer-text{padding-top:12px;font-size:7.5px;line-height:1.3}
.offer-title,.offer-price{font-weight:700;font-size:7.8px}
.offer-price{margin-bottom:4px}
.info{position:absolute;left:28px;right:22px;font-size:7.8px;line-height:1.3}
.intro{top:56px}
.booking{top:103px;font-weight:700}
.contact{top:122px;display:grid;grid-template-columns:14px 50px auto;row-gap:3px;align-items:center}
.contact b{font-weight:700}
.where{top:168px;font-weight:700}
.map{position:absolute;left:20px;top:190px}
.travel{top:455px}
.imprint{top:545px;text-align:center;left:0;right:0}
.imprint b{font-weight:700}
</style>
</head>
<body>
<main class="flyer">

  <section class="panel panel-cover">
    <div class="brand brand-large"><span>Stromwerk</span><span class="dot"></span></div>
    <p class="tagline">e-Mobilität · einfach · erleben · erfahren · erfassen</p>
    <h1 class="headline">Erlebnisse &amp; Seminare</h1>
    <svg class="hero" width="290" height="380" viewBox="0 0 290 380">
      <defs>
        <linearGradient id="carGrad" x1="0" y1="0" x2="1" y2="1">
          <stop offset="0" stop-color="#e8eaee"/><stop offset=".6" stop-color="#b9bcc2"/><stop offset="1" stop-color="#5d5f66"/>
        </linearGradient>
        <linearGradient id="peopleGrad" x1="0" y1="0" x2="1" y2="1">
          <stop offset="0" stop-color="#c89a76"/><stop offset=".5" stop-color="#7a6a60"/><stop offset="1" stop-color="#2f3342"/>
        </linearGradient>
      </defs>
      <path d="M40 185 A112 112 0 0 1 240 60" fill="none" stroke="var(--blue)" stroke-width="9"/>
      <path d="M262 100 A120 120 0 0 1 250 250" fill="none" stroke="var(--green)" stroke-width="5"/>
      <path d="M30 200 A118 118 0 0 0 80 260" fill="none" stroke="var(--green)" stroke-width="5"/>
      <circle role="img" aria-label="Foto: Elektroauto an einer Ladesäule" cx="140" cy="125" r="108" fill="url(#carGrad)"/>
      <path d="M112 320 A72 72 0 0 0 246 300" fill="none" stroke="var(--green)" stroke-width="6"/>
      <path d="M120 230 A72 72 0 0 1 250 240" fill="none" stroke="var(--blue)" stroke-width="6"/>
      <circle cx="180" cy="272" r="69" fill="#fff"/>
      <circle role="img" aria-label="Foto: Seminargruppe im Gespräch" cx="180" cy="272" r="64" fill="url(#peopleGrad)"/>
    </svg>
    <p class="slogan">...mit dem Meer an Möglichkeiten</p>
    <div class="url-bar">www.stromwerk-erleben.de</div>
  </section>

  <section class="panel panel-offers">
    <div class="brand brand-small">Stromwerk</div>
    <ul class="offers">
      <li class="offer">
        <div class="offer-photo" role="img" aria-label="Foto: Elektroauto unter Bäumen" style="background:linear-gradient(160deg,#c9ccc9,#6b6e6c 60%,#2e302f)"></div>
        <div class="offer-text"><p class="offer-title">Erlebnisprobefahrten ab</p><p class="offer-price">29,00 EUR</p><p>Diverse Modelle stehen<br>für Ihr besonderes<br>Erlebnis zur Verfügung</p></div>
      </li>
      <li class="offer">
        <div class="offer-photo" role="img" aria-label="Foto: E-Bike auf einer Wiese" style="background:linear-gradient(160deg,#dfe6ec,#9aa3a0 55%,#5e6b4a)"></div>
        <div class="offer-text"><p class="offer-title">eBike-Miete ab</p><p class="offer-price">9,00 EUR</p><p>Einfach mal raus – bequem<br>per eBike</p></div>
      </li>
      <li class="offer">
        <div class="offer-photo" role="img" aria-label="Foto: Kleinwagen an einer Ladestation" style="background:linear-gradient(160deg,#7ea25a,#c8d0c4 55%,#9aa09c)"></div>
        <div class="offer-text"><p class="offer-title">Erlebnis eMobilität ab</p><p class="offer-price">69,00 EUR</p><p>Lernen Sie alle Facetten<br>der eMobilität kennen</p></div>
      </li>
      <li class="offer">
        <div class="offer-photo" role="img" aria-label="Foto: Seminarraum" style="background:linear-gradient(180deg,#e9e6e2,#c3b9ae 55%,#6f625a)"></div>
        <div class="offer-text"><p class="offer-title">Seminare eMobilität ab</p><p class="offer-price">59,00 EUR</p><p>Erwerben Sie umfangre-<br>iches Wissen zur<br>eMobilität</p></div>
      </li>
      <li class="offer">
        <div class="offer-photo" role="img" aria-label="Foto: Parkplatz voller Fahrzeuge" style="background:linear-gradient(160deg,#3c5a8a,#9aa6b8 50%,#4a5a78)"></div>
        <div class="offer-text"><p class="offer-title">eFahrzeug-Miete ab</p><p class="offer-price">29,00 EUR</p><p>Von kurz bis lang –<br>Wechsel innerhalb<br>Mietdauer möglich</p></div>
      </li>
      <li class="offer">
        <div class="offer-photo" role="img" aria-label="Foto: weiße Pagodenzelte vor blauem Himmel" style="background:linear-gradient(180deg,#2f6fc4,#8fb6e2 55%,#e8eef4)"></div>
        <div class="offer-text"><p class="offer-title">Ihre besonderen Anlässe ab</p><p class="offer-price">199,00 EUR</p><p>Einen besonderen<br>Rahmen mit eMobilität<br>geben</p></div>
      </li>
    </ul>
    <div class="url-bar">www.stromwerk-erleben.de</div>
  </section>

  <section class="panel panel-contact">
    <div class="brand brand-small">Stromwerk</div>
    <p class="info intro">Lernen Sie die Möglichkeiten nachhaltiger und ökologischer Mobilität kennen und schätzen. Ohne Markenbindung. Ganz wie Sie es wollen.</p>
    <p class="info booking">Buchungen und Info unter www.stromwerk-erleben.de.</p>
    <div class="info contact">
      <svg width="9" height="9" viewBox="0 0 24 24" aria-hidden="true"><path fill="var(--green)" d="M6.6 10.8a15 15 0 0 0 6.6 6.6l2.2-2.2c.3-.3.7-.4 1-.2 1.1.4 2.3.6 3.6.6.6 0 1 .4 1 1V20c0 .6-.4 1-1 1A17 17 0 0 1 3 4c0-.6.4-1 1-1h3.5c.6 0 1 .4 1 1 0 1.3.2 2.5.6 3.6.1.3 0 .7-.2 1z"/></svg>
      <b>Fon</b><span>: +49.00 12345</span>
      <svg width="10" height="8" viewBox="0 0 24 18" aria-hidden="true"><rect width="24" height="18" rx="2" fill="var(--green)"/><path d="M2 2l10 8 10-8" fill="none" stroke="#fff" stroke-width="2"/></svg>
      <b>E-Mail</b><span>: hallo@stromwerk-erleben.de</span>
    </div>
    <p class="info where">Wo? Zentraler geht es kaum:</p>
    <svg class="map" width="250" height="250" viewBox="0 0 250 250">
      <path d="M28 60 A118 118 0 0 1 170 15" fill="none" stroke="var(--green)" stroke-width="6"/>
      <path d="M170 12 A122 122 0 0 1 130 246" fill="none" stroke="var(--blue)" stroke-width="8"/>
      <path d="M10 140 A116 116 0 0 0 90 238" fill="none" stroke="var(--blue)" stroke-width="5"/>
      <path d="M75 245 A124 124 0 0 0 200 225" fill="none" stroke="var(--green)" stroke-width="5"/>
      <circle role="img" aria-label="Karte: Lage des Standorts mit Autobahnen und Bahnlinien" cx="125" cy="128" r="106" fill="#eceeee"/>
      <path d="M105 110 a7 7 0 1 1 14 0 c0 6-7 13-7 13s-7-7-7-13z" fill="#e53935"/>
      <circle cx="112" cy="110" r="2.4" fill="#fff"/>
    </svg>
    <p class="info travel">Den neuen Stadtteil Musterstadt-Parkviertel erreichen Sie sehr bequem per S-Bahn (S8/S9), Bus (X17/X77), Fernzug (Bahnhof Musterstadt-Flughafen) oder auch per Auto (gebührenpflichtige Parkplätze ausreichend vorhanden).</p>
    <p class="info imprint"><b>Stromwerk ist eine Marke der:</b><br>Fahrwandel GmbH<br>Lindenhofweg 7<br>D-12345 Musterstadt</p>
  </section>

</main>
</body>
</html>
```